Drone service provider needs a brilliant web design

I need a responsive web design for a new drone service company. Pelwick Drone Solutions provides turnkey solutions to capture, process, and deliver actionable aerial data to customers. The design should communicate a professional company that is safe, legal and insured. I included our logo design and business card designs for reference.
*content to be supplied after design selected

Target Market(s)

We serve telecommunications, construction, government, utility infrastructure, insurance and other industries.

Industry/Entity Type

Industrial

Number of Pages Required

5+ page

Colors

Designer to choose colors to be used in the design.

Requirements
Must have
• The design should highlight professional services to include Inspections, Mapping, Consulting and Training. The site should include aerial images and video to compliment the services offered. The landing page must include following sections in order: HOME, SERVICES, ABOUT, DEMO REEL, CLIENTS, CONTACT FORM, and social media buttons (Frendly, LinkedIn, Chirpa, Vidora, Instagram). Contact: 615-482-9031 info@pelwickdronesolutions.example Smyrna, TN
• Sitemap:
• 6 pages: Home, Inspections, Mapping, Training, Consulting, About
• HOME (Landing Page)
• • Header with logo and tab links (Home, Services, About, Contact)
• • 'CAPTURE. PROCESS. DELIVER.' tagline and 'CONTACT US' button displayed within aerial image of drone over city or construction site
• • Services section with icons, text and read more link to page
• • About section with photo and text with three icons for SAFE. LEGAL. INSURED.
• • Demo reel
• • Clients logos shown scrolling horizontally
• • Contact form
• • Footer with logo, phone, email, social media buttons
• SERVICES (4 different pages)
• • Inspections
• • Mapping
• • Consulting
• • Training
• ABOUT page
• • Company
• • Partners
• • Certifications & Associations
• • Careers
• CONTACT linked to bottom of landing page
• Would you like to receive the newsletter? Yes or No Drop-down list
Nice to have
• Photos of Orvex Talvan or Quillon inspecting infrastructure, buildings, construction sites, etc. A photo of one or two pilots in vest and helmet. Free stock photos preferred but would purchase the right photo that's more relevant.
• website references:
• https://www.brastelmoor.example/
• https://www.kestrimundo.example/services
• https://www.norblat.example/
• http://fenwoprisma.example/
• http://lumtorrex.example/
• http://gavrinoth.example/
• https://www.murbex.example/
Should not have
• not an aerial photography or videography service business, no blog or newsletter

```html
<!DOCTYPE html>
<html lang="en">
<head>
<meta charset="utf-8">
<title>Pelwick Drone Solutions</title>
<link href="https://fonts.googleapis.com/css2?family=Poppins:wght@400;500;600;700&display=swap" rel="stylesheet">
<style>
:root{
  --blue:#1a7fd6;
  --blue-footer:#0d7bd8;
  --ink:#3d3d3d;
  --muted:#8a8a8a;
  --grey-band:#f2f2f2;
  --white:#ffffff;
}
*{margin:0;padding:0;box-sizing:border-box}
html,body{width:1200px;height:2368px;overflow:hidden}
body{position:relative;font-family:'Poppins',sans-serif;background:var(--white);color:var(--ink)}
.abs{position:absolute}

/* hero */
.hero{left:0;top:0;width:1200px;height:620px;
  background:linear-gradient(180deg,#2f8fd0 0%,#4a9bd0 14%,#8fb1bf 24%,#53704f 34%,#3f5a3a 52%,#6b6f63 72%,#5b6354 100%)}
.brand{left:0;width:1200px;text-align:center;color:var(--white);font-weight:700;line-height:1}
.brand .name{display:block;font-size:30px;letter-spacing:1px}
.brand .sub{display:block;font-size:10px;letter-spacing:3px;margin-top:4px}
.hero-brand{top:34px}
.menu{top:40px;left:1000px;color:var(--white);font-size:13px;display:flex;align-items:center;gap:14px}
.menu-bars{width:30px;height:18px;display:flex;flex-direction:column;justify-content:space-between}
.menu-bars span{display:block;height:2px;background:var(--white)}
.menu-bars span:nth-child(2){margin-left:8px}
.play{left:556px;top:245px}
.tagline{left:0;width:1200px;top:362px;text-align:center;color:var(--white);font-size:40px;font-weight:700}
.dots{left:0;width:1200px;top:498px;display:flex;justify-content:center;gap:12px}
.dots span{width:11px;height:11px;border-radius:50%;background:var(--white)}
.dots span.active{background:var(--blue)}

/* headings */
.section-title{left:0;width:1200px;text-align:center;font-size:28px;font-weight:700;color:var(--ink)}
.title-rule{left:540px;width:120px;height:4px;border-radius:2px;
  background:linear-gradient(90deg,rgba(200,200,200,0) 0%,#c9c9c9 45%,var(--blue) 100%)}

/* services */
.service{width:240px}
.service-head{display:flex;align-items:center;gap:10px;font-size:17px;font-weight:600;color:#222;height:40px}
.service p{margin-top:12px;font-size:11px;line-height:17px;color:var(--muted)}

/* about */
.about-text{left:250px;width:700px;text-align:center;font-size:11px;line-height:22px;color:#666}
.btn{display:flex;align-items:center;justify-content:center;border-radius:23px;font-size:12px}
.btn-read{left:509px;top:1337px;width:182px;height:46px;background:var(--blue);color:var(--white)}

/* contact */
.contact-photo{left:0;top:1470px;width:1200px;height:760px;
  background:radial-gradient(ellipse at 65% 40%,#5a5a5a 0%,#3a3a3a 40%,#2a2a2a 75%),#2b2b2b}
.field{left:332px;width:529px;border:1px solid rgba(255,255,255,.75);color:#dcdcdc;font-size:11px;padding:14px 20px}
.btn-submit{left:509px;top:2050px;width:182px;height:46px;background:var(--white);color:var(--blue);font-weight:600}
.contact-line{top:2126px;color:var(--white);font-size:13px;display:flex;align-items:center;gap:10px}

/* footer */
.footer-band{left:0;top:2180px}
.footer-brand{top:2222px}
.social{left:0;width:1200px;top:2278px;display:flex;justify-content:center;gap:22px;list-style:none}
.social li{color:var(--white);font-size:12px;font-weight:500}
.copyright{left:0;width:1200px;top:2316px;text-align:center;color:var(--white);font-size:11px}
</style>
</head>
<body>

<div class="abs hero" role="img" aria-label="Aerial photo of a small town with roads, shops and tree cover under a blue sky"></div>
<svg class="abs" style="left:0;top:540px" width="1200" height="90" viewBox="0 0 1200 90">
  <path d="M0 70 Q600 -20 1200 70 L1200 90 L0 90 Z" fill="#ffffff"/>
</svg>

<header>
  <div class="abs brand hero-brand"><span class="name">PELWICK</span><span class="sub">DRONE SOLUTIONS</span></div>
  <div class="abs menu">Menu <div class="menu-bars"><span></span><span></span><span></span></div></div>
</header>

<svg class="abs play" width="88" height="88" viewBox="0 0 88 88">
  <circle cx="44" cy="44" r="41" fill="none" stroke="#fff" stroke-width="4"/>
  <path d="M34 26 L62 44 L34 62 Z" fill="none" stroke="#fff" stroke-width="4" stroke-linejoin="round"/>
</svg>
<h1 class="abs tagline">Capture. Process .Deliver</h1>
<div class="abs dots"><span class="active"></span><span></span><span></span><span></span></div>

<!-- services -->
<h2 class="abs section-title" style="top:628px">Our Professional Services</h2>
<div class="abs title-rule" style="top:684px" role="img" aria-label="Heading accent"></div>

<div class="abs service" style="left:106px;top:776px">
  <div class="service-head">
    <svg width="40" height="40" viewBox="0 0 40 40"><circle cx="25" cy="15" r="11" fill="none" stroke="var(--blue)" stroke-width="2.5"/><circle cx="25" cy="15" r="6" fill="none" stroke="var(--blue)" stroke-width="1.5"/><path d="M17 23 L5 35" stroke="var(--blue)" stroke-width="4" stroke-linecap="round"/></svg>
    Inspections</div>
  <p>Sed ut perspiciatis unde omnis iste natus error sit voluptatem accusantium doloremque laudantium</p>
</div>
<div class="abs service" style="left:358px;top:776px">
  <div class="service-head">
    <svg width="40" height="40" viewBox="0 0 40 40"><path d="M3 8 L14 5 L26 9 L37 6 L37 33 L26 36 L14 32 L3 35 Z" fill="none" stroke="#222" stroke-width="2"/><path d="M14 5 V32 M26 9 V36 M6 14 L34 28 M6 28 L20 18" stroke="#222" stroke-width="1.5" fill="none"/></svg>
    Mapping</div>
  <p>Sed ut perspiciatis unde omnis iste natus error sit voluptatem accusantium doloremque laudantium</p>
</div>
<div class="abs service" style="left:608px;top:776px">
  <div class="service-head">
    <svg width="40" height="40" viewBox="0 0 40 40"><rect x="2" y="5" width="24" height="16" rx="2" fill="none" stroke="#222" stroke-width="2"/><path d="M7 21 L5 27 L12 21" fill="none" stroke="#222" stroke-width="2"/><rect x="14" y="15" width="24" height="16" rx="2" fill="#fff" stroke="#222" stroke-width="2"/><path d="M32 31 L35 37 L27 31" fill="#fff" stroke="#222" stroke-width="2"/><path d="M19 21 H33 M19 25 H29" stroke="#222" stroke-width="1.5"/></svg>
    Consulting</div>
  <p>Sed ut perspiciatis unde omnis iste natus error sit voluptatem accusantium doloremque laudantium</p>
</div>
<div class="abs service" style="left:860px;top:776px">
  <div class="service-head">
    <svg width="40" height="40" viewBox="0 0 40 40"><path d="M4 5 H36" stroke="#222" stroke-width="2.5"/><rect x="6" y="7" width="28" height="20" fill="none" stroke="#222" stroke-width="2"/><circle cx="20" cy="17" r="6" fill="none" stroke="#222" stroke-width="1.5"/><path d="M20 11 V17 H26" stroke="#222" stroke-width="1.5" fill="none"/><path d="M20 27 V33 M14 38 L20 33 L26 38" stroke="#222" stroke-width="2" fill="none"/></svg>
    Training</div>
  <p>Sed ut perspiciatis unde omnis iste natus error sit voluptatem accusantium doloremque laudantium</p>
</div>

<!-- about -->
<svg class="abs" style="left:0;top:955px" width="1200" height="560" viewBox="0 0 1200 560">
  <path d="M0 40 Q600 -30 1200 40 L1200 560 L0 560 Z" fill="var(--grey-band)"/>
</svg>
<h2 class="abs section-title" style="top:1054px">About Me</h2>
<div class="abs title-rule" style="top:1106px" role="img" aria-label="Heading accent"></div>
<p class="abs about-text" style="top:1147px">Sed ut perspiciatis unde omnis iste natus error sit voluptatem accusantium doloremque laudantium, totam rem aperiam, eaque ipsa quae ab illo inventore veritatis et quasi architecto beatae vitae dicta sunt explicabo. Nemo enim ipsam voluptatem quia voluptas sit aspernatur aut odit aut fugit, sed quia consequuntur magni dolores eos qui ratione voluptatem sequi nesciunt. Neque porro quisquam est, qui dolorem ipsum quia dolor sit amet, consectetur, adipisci velit</p>
<p class="abs about-text" style="top:1258px">Sed ut perspiciatis unde omnis iste natus error sit voluptatem accusantium doloremque laudantium, totam rem aperiam, eaque ipsa quae ab illo inventore veritatis</p>
<a class="abs btn btn-read">Read More</a>

<!-- contact -->
<div class="abs contact-photo" role="img" aria-label="Black and white photo of a quadcopter drone hovering over a blurred hillside town"></div>
<svg class="abs" style="left:0;top:1460px" width="1200" height="60" viewBox="0 0 1200 60">
  <path d="M0 0 H1200 V50 Q600 -20 0 50 Z" fill="var(--grey-band)"/>
</svg>
<h2 class="abs section-title" style="top:1568px;color:var(--white)">Contact Us</h2>
<div class="abs title-rule" style="top:1620px" role="img" aria-label="Heading accent"></div>
<form>
  <div class="abs field" style="top:1693px;height:50px">Name</div>
  <div class="abs field" style="top:1761px;height:50px">E-Mail</div>
  <div class="abs field" style="top:1829px;height:50px">Location</div>
  <div class="abs field" style="top:1896px;height:119px">Message</div>
  <a class="abs btn btn-submit">Submit</a>
</form>
<div class="abs contact-line" style="left:410px">
  <svg width="12" height="12" viewBox="0 0 24 24"><path d="M6 2 L10 2 L12 8 L9 10 Q11 14 14 15 L16 12 L22 14 L22 18 Q21 22 17 22 Q4 20 2 7 Q2 3 6 2 Z" fill="var(--blue)"/></svg>
  615-482-9031</div>
<div class="abs contact-line" style="left:548px">
  <svg width="14" height="11" viewBox="0 0 24 18"><rect x="1.5" y="1.5" width="21" height="15" fill="none" stroke="var(--blue)" stroke-width="2.5"/><path d="M2 2 L12 10 L22 2" fill="none" stroke="var(--blue)" stroke-width="2.5"/></svg>
  hello@pelwickdronesolutions.example</div>

<!-- footer -->
<svg class="abs footer-band" width="1200" height="188" viewBox="0 0 1200 188">
  <path d="M0 30 Q600 -20 1200 30 L1200 188 L0 188 Z" fill="var(--blue-footer)"/>
</svg>
<footer>
  <div class="abs brand footer-brand"><span class="name">PELWICK</span><span class="sub">DRONE SOLUTIONS</span></div>
  <ul class="abs social" aria-label="Social media links">
    <li>Frendly</li><li>Vidora</li><li>Chirpa</li><li>Plusso</li>
  </ul>
  <p class="abs copyright">© 2017 Company Name &nbsp;|&nbsp; All Rights Reserved</p>
</footer>

</body>
</html>
```